Boutique Health and Fitness Personal Training Studio

I would like to have a brochure designed which provides a detailed description of the services offered in my business.
I have personal training studio, We look after people from early 20's to 90's, healthy to very unhealthy.
We conduct:
A consultation
An assessment
A personalised program
Personalised training sessions
I would like to base the design around the colours of my logo (attached) and use some of (or all of) the images and information I have also attached.
I would be happy with your own images included also.

Target Market(s)

20 to 90 year olds

Industry/Entity Type

Business

Font styles to use
Serif
Sans Serif

Colors
9bcb3c
add136
cadf82
eaf2ce

Requirements
Must have
• Colour and images of fitness.
• 8.5x14 legal
• Tri fold
• 2 folds with 3 faces back n front
Nice to have
• The feeling of wellbeing
Should not have
• This is not a gym.
• It should have the feel of a private relaxed environment

```html
<!DOCTYPE html>
<html lang="en">
<head>
<meta charset="utf-8">
<title>Evergreen Wellness Studio – Brochure Back</title>
<link href="https://fonts.googleapis.com/css2?family=Montserrat:wght@400;600;700&display=swap" rel="stylesheet">
<style>
  :root {
    --green: #9bcb3c;
    --green-lime: #add136;
    --green-soft: #cadf82;
    --green-pale: #eaf2ce;
    --green-deep: #6ea42c;
    --text-dark: #222;
    --text-light: #ffffff;
    --heading-on-green: #e3f53a;
    --page-bg: #e9e9e6;
  }
  html, body {
    margin: 0;
    width: 1200px;
    height: 876px;
    overflow: hidden;
    background: var(--page-bg);
  }
  .brochure {
    position: absolute;
    left: 10px;
    top: 76px;
    width: 1422px;
    height: 872px;
    transform: scale(0.83);
    transform-origin: top left;
    background: #fff;
    font-family: "Montserrat", sans-serif;
    box-shadow: 0 6px 18px rgba(0,0,0,0.18);
    overflow: hidden;
  }
  .brochure-art {
    position: absolute;
    inset: 0;
    width: 1422px;
    height: 872px;
  }
  .block {
    position: absolute;
  }
  .heading {
    margin: 0;
    font-weight: 700;
    font-size: 20px;
    line-height: 25px;
    color: var(--green);
  }
  .body-copy {
    margin: 0;
    font-weight: 400;
    font-size: 15.5px;
    line-height: 23px;
    color: var(--text-dark);
  }
  .panel-care .block { left: 25px; width: 445px; }
  .panel-steps .block { left: 496px; width: 440px; }
  .panel-steps .heading { color: var(--heading-on-green); }
  .panel-steps .body-copy { color: var(--text-light); }
  .nutrition { left: 964px; top: 32px; width: 320px; }
  .nutrition .body-copy { line-height: 27.8px; }
  .studio-name {
    position: absolute;
    left: 86px;
    top: 782px;
    display: flex;
    align-items: center;
    gap: 10px;
    font-weight: 600;
    font-size: 20px;
    color: var(--green-deep);
  }
  .studio-name .dot {
    width: 30px;
    height: 30px;
    border-radius: 50%;
    background: var(--green);
  }
  .sessions-title {
    position: absolute;
    left: 1074px;
    top: 623px;
    width: 348px;
    height: 52px;
    margin: 0;
    background: var(--green);
    color: #fff;
    font-weight: 700;
    font-size: 33px;
    line-height: 52px;
    text-align: center;
  }
  .sessions-copy {
    position: absolute;
    right: 35px;
    top: 684px;
    width: 440px;
    margin: 0;
    text-align: right;
    font-size: 15.5px;
    line-height: 27.8px;
    color: var(--text-dark);
  }
</style>
</head>
<body>
<div class="brochure">
  <svg class="brochure-art" viewBox="0 0 1422 872" xmlns="http://www.w3.org/2000/svg">
    <defs>
      <linearGradient id="gym-dark" x1="0" y1="0" x2="1" y2="1">
        <stop offset="0" stop-color="#3a3f3c"/>
        <stop offset="0.5" stop-color="#6b5a4c"/>
        <stop offset="1" stop-color="#2b2e2c"/>
      </linearGradient>
      <linearGradient id="faint-portrait" x1="0" y1="0" x2="1" y2="1">
        <stop offset="0" stop-color="#ffffff"/>
        <stop offset="0.5" stop-color="#eeeeec"/>
        <stop offset="1" stop-color="#f6f3f0"/>
      </linearGradient>
      <linearGradient id="coach-photo" x1="0" y1="0" x2="1" y2="0">
        <stop offset="0" stop-color="#d9dcdc"/>
        <stop offset="0.35" stop-color="#c8283a"/>
        <stop offset="0.6" stop-color="#d83447"/>
        <stop offset="1" stop-color="#f3f3f3"/>
      </linearGradient>
      <linearGradient id="green-panel" x1="0" y1="0" x2="0" y2="1">
        <stop offset="0" stop-color="#8cc63a"/>
        <stop offset="0.55" stop-color="#80b632"/>
        <stop offset="1" stop-color="#6fa62a"/>
      </linearGradient>
      <linearGradient id="waist-photo" x1="0" y1="0" x2="0" y2="1">
        <stop offset="0" stop-color="#f0dcd2"/>
        <stop offset="0.5" stop-color="#d99a80"/>
        <stop offset="1" stop-color="#d0405a"/>
      </linearGradient>
      <linearGradient id="green-band" x1="0" y1="0" x2="1" y2="0">
        <stop offset="0" stop-color="#5f9a25"/>
        <stop offset="1" stop-color="#8cc63a"/>
      </linearGradient>
      <linearGradient id="training-duo" x1="0" y1="0" x2="1" y2="0">
        <stop offset="0" stop-color="#1f3a10"/>
        <stop offset="0.6" stop-color="#3d6b1c"/>
        <stop offset="1" stop-color="#6ea42c" stop-opacity="0"/>
      </linearGradient>
      <linearGradient id="faint-figures" x1="0" y1="0" x2="0" y2="1">
        <stop offset="0" stop-color="#ececec"/>
        <stop offset="1" stop-color="#f7f7f7"/>
      </linearGradient>
    </defs>

    <!-- left panel -->
    <rect x="0" y="0" width="478" height="872" fill="#ffffff"/>
    <rect role="img" aria-label="Faint portrait of a smiling man behind the text" x="150" y="360" width="328" height="512" fill="url(#faint-portrait)"/>
    <polygon role="img" aria-label="Man exercising on a cable machine in the studio" points="0,0 478,0 478,295 0,118" fill="url(#gym-dark)"/>
    <polygon points="0,116 478,293 478,303 0,126" fill="var(--green)"/>

    <!-- centre panel -->
    <rect x="478" y="0" width="467" height="872" fill="url(#green-panel)"/>
    <polygon role="img" aria-label="Trainer guiding a client's posture during an exercise" points="478,0 945,0 945,125 478,300" fill="url(#coach-photo)"/>
    <polygon points="478,296 945,121 945,129 478,304" fill="var(--heading-on-green)"/>

    <!-- right panel -->
    <rect x="945" y="0" width="477" height="872" fill="#ffffff"/>
    <polygon role="img" aria-label="Woman measuring her waist with a tape" points="1240,0 1422,0 1422,235 1240,297" fill="url(#waist-photo)"/>
    <polygon points="945,397 1422,235 1422,480 945,662" fill="url(#green-band)"/>
    <polygon role="img" aria-label="Trainer and client doing a lunge exercise together" points="945,520 1100,410 1260,400 1310,420 1200,560 945,662" fill="url(#training-duo)" opacity="0.85"/>
    <rect role="img" aria-label="Faint figures of people training with an exercise ball" x="1150" y="560" width="272" height="312" fill="url(#faint-figures)" opacity="0.7"/>
    <polygon points="945,662 1422,480 1422,560 1150,675 945,675" fill="#ffffff" opacity="0"/>
  </svg>

  <section class="panel-care">
    <div class="block" style="top:238px">
      <h2 class="heading">Personalised Care<br>in Fitness and Health</h2>
      <p class="body-copy" style="margin-top:4px">Exercise programs for all levels of health and fitness and all age groups. Experience in managing a wide range of chronic health conditions.</p>
    </div>
    <div class="block" style="top:385px">
      <h2 class="heading">Experienced professionals<br>caring for your wellbeing</h2>
      <p class="body-copy" style="margin-top:4px">Exercise Physiologist with over 25 years of experience managing the health and fitness needs of the community.</p>
    </div>
    <div class="block" style="top:532px">
      <h2 class="heading">What to Expect</h2>
      <p class="body-copy" style="margin-top:6px">On arrival at the studio you will be asked to complete a questionnaire, which will provide us with information regarding your background with health and fitness, as well as your goals and objectives.</p>
      <p class="body-copy" style="margin-top:23px">Please bring any relevant medical information from medical practitioners or health professionals that you feel may impact on your program.</p>
    </div>
    <div class="studio-name"><span class="dot"></span>Evergreen Wellness Studio</div>
  </section>

  <section class="panel-steps">
    <div class="block" style="top:317px">
      <h2 class="heading">Consultation</h2>
      <p class="body-copy" style="margin-top:5px">A consultation will allow you to share your thoughts, concerns and objectives, as well as provide you with ample opportunity to expand on the answers from your questionnaire relating to your prior and current health, medical and physical concerns.</p>
    </div>
    <div class="block" style="top:486px">
      <h2 class="heading">Assessment</h2>
      <p class="body-copy" style="margin-top:5px">An assessment will be conducted to provide us both with a baseline measure of your cardiovascular fitness, strength, flexibility, balance and body composition measures. These measures provide us with a reference for program design and also to indicate improvements along the way.</p>
    </div>
    <div class="block" style="top:676px">
      <h2 class="heading">The Program</h2>
      <p class="body-copy" style="margin-top:5px">Your program will be designed with consideration to your health and fitness background, you objectives and your strengths and weaknesses. It will be personally tailored to your needs and provide you with a plan to focus your energies on.</p>
    </div>
  </section>

  <section class="panel-sessions">
    <div class="block nutrition">
      <h2 class="heading">Nutrition</h2>
      <p class="body-copy" style="margin-top:4px">Nutrition is central to an effective program, as it will provide you with maximal energy for exercise as well as keeping yourself lean and healthy for a long term fitter lifestyle. Evergreen Wellness Studio provides initial monitoring and ongoing modification in accordance with your needs.</p>
    </div>
    <h2 class="sessions-title">YOUR SESSIONS</h2>
    <p class="sessions-copy">Training at the studio is professional and caring,<br>but focused and challenging. Typically each<br>session will take approximately 60 minutes.<br>Training times can be organized to suit your needs<br>with early mornings and evenings available.</p>
  </section>
</div>
</body>
</html>
```